Natural Australian skin care company packaging for new product Bath salts

We are moving to fully refillable packaging and need someone to design our refill pouches. we have a number of products we need to do this for but our first one is our natural bath salts. This comes in a 200g tin in a pouch then the pouch can be bought to refill the tin. We can either print on the pouch or do sickers. The tin is a simple matt black tin with white text on the lid. the pouch comes in a gold colour. pictures are in the file vault lid.
Luxury bath salts Pouch - the dimensions are 60*55*180mm, , we can either print directly or do a sticker, We also need the sleeve to go around the tin. The dimensions of the tin are 65x65x70mm. The same text needs to go onto the sleeve as the pouch. The tin is black with white printing on the top (see picture).
Text is as follows
VT logo Pale marsh reed 100% pure magnesium bath salts
A rich fragrance of Australian wild flowers (using natural essential oils) with frangipani and gardenia. Sink into the natural ancient salt lake sourced 100% pure magnesium to replenish your skin. Transdermal absorption of magnesium is effective and contributes to electrolyte balance, normal muscle function and aids calcium absorption. The ultimate mineral reset.
Directions: Fill bath, once full put two heaped tablespoons of the salts into the bath (approx 50g). Climb in and relax.
Vell Tonic full logo
Country of Origin: Australia
PO Box 318
Kelvale Shore 4861
QLD Australia
www.velltonic-example.com
ingredients:
magnesium chloride *, parfum **
*naturally sourced from ancient salt lakes
**a combination of essential oils and natural isolates.
e: 200g / 7.05 Oz
We also need the recycle, plastic free, not tested on animal eco friendly symbols.
Please use this link to our press assets and tin and pouch photos.
https://www.filevault-example.com/sh/kq3tn481pwzdb57/QQmxT__wLsVbnaKe-RtyHdZpc?dl=0

```html
<!DOCTYPE html>
<html lang="en">
<head>
<meta charset="utf-8">
<title>Vell Tonic – Bath Salts Sticker Draft</title>
<link href="https://fonts.googleapis.com/css2?family=Arvo:wght@700&family=Caveat+Brush&family=Josefin+Sans:wght@300;400;600&family=Pathway+Gothic+One&display=swap" rel="stylesheet">
<style>
  :root {
    --page-bg: #ffffff;
    --label-bg: #a6ebe8;
    --label-bg-soft: #b8f0ed;
    --ink: #111111;
    --heading-grey: #4a4a4a;
    --scent-teal: #1f9c97;
    --band-teal: #1b8a86;
    --band-text: #c9f4f1;
    --salt-light: #d6f7f5;
    --flower-blue: #9fb4d8;
    --flower-green: #7fa86a;
  }
  * { margin: 0; padding: 0; box-sizing: border-box; }
  html, body { width: 1200px; height: 800px; overflow: hidden; background: var(--page-bg); }
  .canvas { position: relative; width: 1200px; height: 800px; }

  .draft-heading {
    position: absolute; top: 34px; left: 0; width: 1200px; text-align: center;
    font-family: "Josefin Sans", sans-serif; font-weight: 300; color: var(--heading-grey);
  }
  .draft-heading__title { font-size: 40px; letter-spacing: 6px; line-height: 1.1; }
  .draft-heading__sub { font-size: 28px; letter-spacing: 2px; line-height: 1.1; }

  .sticker {
    position: absolute; left: 318px; top: 150px; width: 563px; height: 621px;
    border-radius: 24px; overflow: hidden;
    background: radial-gradient(ellipse at 50% 35%, var(--label-bg-soft), var(--label-bg) 70%);
  }
  .sticker > * { position: absolute; }

  .brand { top: 46px; left: 0; width: 100%; text-align: center; color: var(--ink); font-family: "Arvo", serif; font-weight: 700; }
  .brand__name { font-size: 35px; letter-spacing: 0.5px; line-height: 1; }
  .brand__tagline { font-size: 11.5px; margin-top: 8px; letter-spacing: 0.2px; }

  .product-claim { top: 205px; left: 0; width: 100%; text-align: center; font-family: "Josefin Sans", sans-serif; font-weight: 400; font-size: 25px; color: var(--ink); }
  .product-name { top: 232px; left: 0; width: 100%; text-align: center; font-family: "Caveat Brush", cursive; font-size: 98px; line-height: 1; color: var(--ink); letter-spacing: 2px; }

  .scent { top: 360px; left: 0; width: 100%; text-align: center; font-family: "Josefin Sans", sans-serif; font-weight: 400; font-size: 34px; color: var(--scent-teal); }
  .scent-band { top: 396px; left: 144px; width: 284px; height: 48px; }
  .scent-band__text { top: 404px; left: 144px; width: 284px; text-align: center; font-family: "Josefin Sans", sans-serif; font-size: 17px; color: var(--band-text); }

  .illustration-flowers-left { left: 0; top: 367px; width: 135px; height: 254px; background: linear-gradient(160deg, var(--flower-blue), var(--flower-green)); opacity: 0.75; border-top-right-radius: 60px; }
  .illustration-flowers-right { left: 451px; top: 251px; width: 112px; height: 370px; background: linear-gradient(200deg, var(--flower-blue), var(--flower-green)); opacity: 0.75; border-top-left-radius: 60px; }
  .illustration-salt { left: 107px; top: 467px; width: 168px; height: 168px; border-radius: 50%; background: radial-gradient(circle, #ffffff, var(--salt-light) 70%); opacity: 0.85; }

  .net-weight { left: 316px; top: 528px; font-family: "Pathway Gothic One", sans-serif; font-size: 28px; line-height: 1.05; color: var(--ink); }
  .net-weight__estimated { font-family: "Josefin Sans", sans-serif; font-size: 22px; margin-left: 6px; }
</style>
</head>
<body>
<main class="canvas">
  <header class="draft-heading">
    <div class="draft-heading__title">DRAFT DESIGN</div>
    <div class="draft-heading__sub">(STICKER)</div>
  </header>

  <section class="sticker" aria-label="Bath salts pouch sticker">
    <div class="illustration-flowers-left" role="img" aria-label="Vintage illustration of blue forget-me-not flowers on green stems"></div>
    <div class="illustration-flowers-right" role="img" aria-label="Vintage illustration of blue forget-me-not flowers with leaves"></div>
    <div class="illustration-salt" role="img" aria-label="Pile of white magnesium bath salt crystals"></div>

    <div class="brand">
      <div class="brand__name">VELL TONIC</div>
      <div class="brand__tagline">AUSTRALIAN NATURAL SKINCARE</div>
    </div>

    <div class="product-claim">100% pure magnesium</div>
    <h1 class="product-name">BATH SALTS</h1>

    <div class="scent">Scentname</div>
    <svg class="scent-band" viewBox="0 0 284 48" aria-hidden="true">
      <path d="M8 6 L276 2 L284 20 L262 30 L270 38 L40 46 L0 44 L14 32 L2 24 Z" fill="var(--band-teal)"/>
    </svg>
    <div class="scent-band__text">with natural essential oils</div>

    <div class="net-weight">
      NET WT<br>7.05 OZ. (200g)<span class="net-weight__estimated">e</span>
    </div>
  </section>
</main>
</body>
</html>
```